Halvern Dental website redesign

We need a redesign for a website: myhalverndental.com.

I already created a video going over what exactly is needed in the design.

See Video here: https://files.quorvane.com/file/d/8xKpQ2mWn4TzLrV7bHsYcE3jFuGaD6oN1/view?usp=sharing

Reviewly Slide shown in Video: https://slides.quorvane.com/presentation/d/7RtW2yQnXbVc4LmPz9KsHdJf3GaE8oUi6TeYqNvB5wZx/edit?usp=sharing
Updates

Holidays in India so we did not get enough design entries or quality.

Target Market(s)

Dentistry

Industry/Entity Type

Dentistry

Number of Pages Required

1 page

Colors
0094D4
00A9DD
6FCCEA
C7EBF8
E9F6FB
00AB8E
00BBA5
67D7C9
C6EFE9
E9F9F6

Requirements
Must have
• See 13 min video link in description - shows what to do.

```html
<!DOCTYPE html>
<html lang="en">
<head>
<meta charset="utf-8">
<title>Halvern Dental</title>
<link href="https://fonts.googleapis.com/css2?family=Montserrat:wght@400;500;600;700;800&family=Roboto:wght@400;500;700&display=swap" rel="stylesheet">
<style>
:root{
  --blue:#0094d4;
  --blue-2:#00a9dd;
  --blue-3:#6fccea;
  --blue-pale:#e9f4fb;
  --teal:#00bba5;
  --teal-2:#00ab8e;
  --green:#78b83a;
  --red:#d81f26;
  --ink:#333;
  --body:#555;
  --navy:#0d5f86;
  --white:#fff;
}
*{margin:0;padding:0;box-sizing:border-box}
html,body{width:1200px;height:3728px;overflow:hidden}
body{position:relative;font-family:"Roboto",Arial,sans-serif;color:var(--body);background:var(--white)}
.abs{position:absolute}
h1,h2,h3,.head{font-family:"Montserrat",Arial,sans-serif}

/* header */
.site-header{position:absolute;left:0;top:0;width:1200px;height:106px;background:var(--white);border-bottom:1px solid #e6e6e6}
.brand{position:absolute;left:92px;top:30px;display:flex;align-items:center;gap:10px;font-family:"Montserrat",sans-serif;font-weight:700;font-size:26px;color:var(--green)}
.brand-dot{width:14px;height:14px;border-radius:50%;background:var(--red)}
.phone-tab{position:absolute;left:598px;top:0;width:202px;height:54px;background:var(--teal);border-radius:0 0 40px 40px;color:#fff;font-weight:500;font-size:17px;display:flex;align-items:center;justify-content:center;gap:8px}
.top-btn{position:absolute;top:7px;height:36px;border-radius:18px;color:#fff;font-weight:700;font-size:13px;display:flex;align-items:center;justify-content:center}
.btn-schedule{left:815px;width:133px;background:var(--blue-2)}
.btn-emergency{left:965px;width:145px;background:var(--red)}
.main-nav a{position:absolute;top:68px;font-size:14px;color:#555;text-decoration:none;white-space:nowrap}
.nav-active{position:absolute;left:316px;top:102px;width:76px;height:4px;background:var(--teal)}
.caret{display:inline-block;margin-left:4px;border:4px solid transparent;border-top-color:#999;vertical-align:-2px}

/* hero */
.hero{position:absolute;left:0;top:106px;width:1200px;height:570px;background:linear-gradient(160deg,#5fe0f4 0%,#1ea6e8 35%,#0a7fd4 100%)}
.hero-art{position:absolute;left:580px;top:52px;width:492px;height:452px;border-radius:45% 45% 30% 30%;background:radial-gradient(ellipse at 50% 45%,rgba(255,255,255,.35),rgba(255,255,255,.06) 70%,transparent 72%)}
.hero h1{position:absolute;left:106px;top:140px;font-size:49px;line-height:53px;font-weight:800;color:#fff}
.hero .lede{position:absolute;left:108px;top:256px;font-family:"Montserrat",sans-serif;font-size:23px;line-height:31px;color:#fff}
.btn{position:absolute;border-radius:28px;color:#fff;font-family:"Montserrat",sans-serif;font-weight:700;font-size:13px;display:flex;align-items:center;justify-content:center;letter-spacing:.2px}
.btn-green{left:104px;top:330px;width:232px;height:53px;background:var(--green)}

/* section title */
.section-title{position:absolute;left:0;width:1200px;text-align:center;font-size:35px;font-weight:700;color:var(--blue)}
.title-rule{position:absolute;width:52px;height:3px;background:var(--teal);left:574px}

/* team */
.member-name{position:absolute;left:0;width:1200px;text-align:center;top:840px;font-family:"Montserrat",sans-serif;font-weight:700;font-size:20px;color:#444}
.member-role{position:absolute;left:0;width:1200px;text-align:center;top:869px;font-family:"Montserrat",sans-serif;font-size:16px;color:#444}
.portrait{position:absolute;top:912px;height:282px;border-radius:110px 110px 0 0}
.portrait-side{background:linear-gradient(#e9edf0,#f6f7f8);opacity:.7}
.portrait-main{background:linear-gradient(#4a3a36 0%,#2d2f3c 55%,#23252f 100%)}
.chev{position:absolute;top:940px}

/* bio */
.bio{position:absolute;left:0;top:1194px;width:1200px;height:456px;background:var(--blue-pale)}
.bio-meet{position:absolute;left:124px;top:75px;font-family:"Montserrat",sans-serif;font-size:22px;color:#444}
.bio-name{position:absolute;left:124px;top:110px;font-family:"Montserrat",sans-serif;font-weight:700;font-size:27px;color:#333}
.bio-role{position:absolute;left:124px;top:142px;font-family:"Montserrat",sans-serif;font-size:21px;color:var(--blue)}
.bio-divider{position:absolute;left:401px;top:77px;width:1px;height:281px;background:#cfd6dc}
.bio-text{position:absolute;left:450px;top:77px;width:616px;font-size:12.5px;line-height:15px;color:#555}
.bio-text p{margin-bottom:17px}
.member-of{position:absolute;font-size:12px;color:#444;display:flex;align-items:center;gap:8px;white-space:nowrap}

/* services */
.service{position:absolute;width:223px;height:95px;background:var(--teal);color:#fff;font-family:"Montserrat",sans-serif;font-weight:700;font-size:16px;line-height:18px;display:flex;align-items:center;gap:16px;padding-left:28px}
.service svg{flex:none}
.service-active{background:linear-gradient(135deg,#3a9ef0,#1c8be0);box-shadow:0 6px 16px rgba(0,120,220,.35)}

/* experience */
.experience{position:absolute;left:0;top:2193px;width:1200px;height:644px;background:linear-gradient(180deg,#0ba6de 0%,#0a92d3 60%,#0a8bcd 100%)}
.experience h2{position:absolute;left:128px;top:108px;font-size:33px;line-height:38px;font-weight:700;color:#fff}
.experience h2 span{font-weight:400}
.exp-rule{position:absolute;left:129px;top:192px;width:52px;height:3px;background:#fff}
.exp-text{position:absolute;left:129px;top:219px;width:565px;font-size:12.5px;line-height:17px;color:#fff}
.exp-text p{margin-bottom:17px}
.review-card{position:absolute;left:771px;top:91px;width:305px;height:443px;background:#fff}
.rc-title{position:absolute;left:0;width:305px;top:14px;text-align:center;font-family:"Montserrat",sans-serif;font-weight:700;font-size:14px;color:#333}
.stars{color:#f7b500;letter-spacing:3px}
.rc-rating{position:absolute;left:0;width:305px;top:36px;text-align:center;font-size:17px;font-weight:700;color:#333}
.rc-count{position:absolute;left:0;width:305px;top:74px;display:flex;justify-content:center;align-items:center;gap:6px;font-size:11px;color:#444}
.rc-count i{width:15px;height:15px;border-radius:50%;background:var(--blue);display:inline-block}
.rc-sources{position:absolute;left:66px;top:110px;width:188px;height:39px;background:#fff;box-shadow:0 1px 5px rgba(0,0,0,.18);display:flex;align-items:center;justify-content:space-around;font-size:11px;font-weight:700;color:#555}
.rc-review{position:absolute;left:53px;top:159px;width:214px;height:220px;background:#fff;box-shadow:0 1px 8px rgba(0,0,0,.15)}
.rc-avatar{position:absolute;left:13px;top:13px;width:52px;height:52px;border-radius:50%;background:linear-gradient(#b9936f,#8d6a55)}
.rc-stars{position:absolute;left:76px;top:15px;font-size:15px}
.rc-name{position:absolute;left:76px;top:53px;font-family:"Montserrat",sans-serif;font-weight:700;font-size:13px;color:#333}
.rc-quote{position:absolute;left:13px;top:86px;width:190px;font-size:8.4px;line-height:10px;color:#555}
.rc-quote b{color:var(--blue);font-weight:400}
.rc-date{position:absolute;left:13px;top:176px;font-size:8.5px;color:#888}
.rc-source{position:absolute;left:66px;top:380px;width:188px;display:flex;justify-content:space-between;align-items:center;font-size:9.5px;color:#555}
.rc-source strong{font-family:"Montserrat",sans-serif;font-size:19px;font-weight:500;color:var(--blue)}
.rc-arrow{position:absolute;top:250px}

/* excellence */
.excellence{position:absolute;left:0;top:2837px;width:1200px;height:423px;background:linear-gradient(160deg,#2a7f98 0%,#1b6b88 50%,#155e7f 100%)}
.excellence h2{position:absolute;left:0;width:1200px;top:124px;text-align:center;color:#fff;font-size:36px;font-weight:700}
.excellence h2 span{font-weight:400}
.excellence .sub{position:absolute;left:0;width:1200px;top:173px;text-align:center;font-family:"Montserrat",sans-serif;color:#fff;font-size:20px}
.btn-teal{left:476px;top:219px;width:238px;height:52px;background:var(--teal)}

/* footer */
.footer-head{position:absolute;top:3320px;font-family:"Montserrat",sans-serif;font-weight:600;font-size:18px;color:var(--navy)}
.footer-rule{position:absolute;top:3356px;height:2px;background:var(--blue-3)}
.f-line{position:absolute;font-size:12.5px;line-height:20px;color:#444}
.btn-red{left:145px;top:3522px;width:205px;height:37px;background:var(--red);font-size:12px}
.hours span{position:absolute;font-size:12.5px;color:#444}
.map{position:absolute;left:772px;top:3376px;width:305px;height:182px;background:linear-gradient(135deg,#eef1f3,#e3e8ec);border:1px solid #cfd6db}
.bottom-bar{position:absolute;left:0;top:3619px;width:1200px;height:1px;background:#e4e4e4}
.bottom-nav a{position:absolute;top:3650px;font-size:12.5px;color:#444;text-decoration:none;white-space:nowrap}
.social{position:absolute;top:3647px;width:23px;height:23px;border-radius:50%;background:var(--green)}
.copy{position:absolute;left:148px;top:3688px;font-size:9.5px;color:#555}
</style>
</head>
<body>

<header class="site-header">
  <div class="brand"><span class="brand-dot"></span>Halvern Dental</div>
  <div class="phone-tab">
    <svg width="20" height="20" viewBox="0 0 20 20"><circle cx="10" cy="10" r="10" fill="#fff"/><path d="M6.5 5.5l2 0 1 2.5-1.3 1a6 6 0 0 0 2.8 2.8l1-1.3 2.5 1 0 2c-4.5.4-8.4-3.5-8-8z" fill="#00bba5"/></svg>
    (555) 014-7720
  </div>
  <div class="top-btn btn-schedule">Schedule Online</div>
  <div class="top-btn btn-emergency">Emergency</div>
  <nav class="main-nav">
    <a style="left:316px">About Us<span class="caret"></span></a>
    <a style="left:414px">Services<span class="caret"></span></a>
    <a style="left:505px">Financing</a>
    <a style="left:606px">Testimonials</a>
    <a style="left:722px">New Patient Visit</a>
    <a style="left:870px">Specials</a>
    <a style="left:961px">Contact Us</a>
    <a style="left:1070px">Blog</a>
  </nav>
  <div class="nav-active"></div>
</header>

<section class="hero">
  <div class="hero-art" role="img" aria-label="Glowing wireframe tooth illustration"></div>
  <h1>CREATING<br>HEALTHIER SMILES</h1>
  <p class="lede">With Advanced Technology and<br>Affordable Treatment</p>
  <div class="btn btn-green">BOOK AN APPOINTMENT</div>
</section>

<h2 class="section-title" style="top:726px">Meet Our Team</h2>
<div class="title-rule" style="top:772px"></div>
<div class="member-name">Dr. Anika Ravel</div>
<div class="member-role">Endodontist</div>
<svg class="chev" style="left:144px" width="22" height="44" viewBox="0 0 22 44"><path d="M20 2L3 22l17 20" fill="none" stroke="#6fccea" stroke-width="3"/></svg>
<svg class="chev" style="left:1034px" width="22" height="44" viewBox="0 0 22 44"><path d="M2 2l17 20L2 42" fill="none" stroke="#6fccea" stroke-width="3"/></svg>
<div class="portrait portrait-side" style="left:195px;width:268px" role="img" aria-label="Portrait of a male dentist in a white coat"></div>
<div class="portrait portrait-side" style="left:738px;width:246px" role="img" aria-label="Portrait of a female dentist in a white coat"></div>
<div class="portrait portrait-main" style="left:465px;width:244px" role="img" aria-label="Portrait of Dr. Anika Ravel in a dark suit"></div>

<section class="bio">
  <div class="bio-meet">Meet</div>
  <div class="bio-name">Dr. Anika Ravel</div>
  <div class="bio-role">Endodontist</div>
  <div class="bio-divider"></div>
  <div class="bio-text">
    <p>Dr. Ravel received her specialty training in Endodontics from Westbrook University. She graduated with a Master of Science in dentistry degree, in endodontics. She has practiced in Southern California for many years as a general dentist before specializing in endodontics and uses her experience to help her patients make the right decisions, regarding their treatment plans. She is gentle, compassionate and is committed to providing the optimum care for her patients.</p>
    <p>Dr. Ravel is a member of several professional and service organizations, including:</p>
    <p>Dr. Ravel is an active member of the Guild of Root Care Specialists and keeps herself updated with the latest methods and technologies in endodontics. In her free time, Dr. Ravel enjoys cooking, travelling, and spending time with her family.</p>
    <p>Dr. Ravel is a member of several professional and service organizations, including:</p>
  </div>
  <div class="member-of" style="left:450px;top:316px"><svg width="20" height="20" viewBox="0 0 20 20"><circle cx="10" cy="10" r="9" fill="none" stroke="#00bba5" stroke-width="1.5"/><path d="M6 10l3 3 5-6" fill="none" stroke="#00bba5" stroke-width="1.5"/></svg>Continental Dental Guild (CDG)</div>
  <div class="member-of" style="left:450px;top:343px"><svg width="20" height="20" viewBox="0 0 20 20"><circle cx="10" cy="10" r="9" fill="none" stroke="#00bba5" stroke-width="1.5"/><path d="M6 10l3 3 5-6" fill="none" stroke="#00bba5" stroke-width="1.5"/></svg>Pacific Coast Dental League (PDL)</div>
  <div class="member-of" style="left:725px;top:314px"><svg width="20" height="20" viewBox="0 0 20 20"><circle cx="10" cy="10" r="9" fill="none" stroke="#00bba5" stroke-width="1.5"/><path d="M6 10l3 3 5-6" fill="none" stroke="#00bba5" stroke-width="1.5"/></svg>Southern Dental Circle (SDC)</div>
  <div class="member-of" style="left:725px;top:341px"><svg width="20" height="20" viewBox="0 0 20 20"><circle cx="10" cy="10" r="9" fill="none" stroke="#00bba5" stroke-width="1.5"/><path d="M6 10l3 3 5-6" fill="none" stroke="#00bba5" stroke-width="1.5"/></svg>Harbor County Dental Forum (HDF)</div>
</section>

<h2 class="section-title" style="top:1707px">Our Services</h2>
<div class="title-rule" style="top:1753px"></div>

<div class="services">
  <div class="service service-active" style="left:127px;top:1790px"><svg width="40" height="44" viewBox="0 0 40 44"><path d="M8 4c5-3 9 0 12 0s7-3 12 0c4 3 2 10 0 13H8C6 14 4 7 8 4zM10 21h20M14 25v15l3-4 3 4 3-4 3 4V25" fill="none" stroke="#fff" stroke-width="2"/></svg>DENTAL<br>IMPLANTS</div>
  <div class="service" style="left:365px;top:1790px"><svg width="46" height="44" viewBox="0 0 46 44"><path d="M6 20c0 12 8 20 17 20s17-8 17-20M12 22v6M18 24v8M24 24v8M30 24v8M36 22v6M6 4h18v8H6zM24 8h14" fill="none" stroke="#fff" stroke-width="2"/></svg>COSMETIC<br>DENTISTRY</div>
  <div class="service" style="left:604px;top:1790px"><svg width="44" height="46" viewBox="0 0 44 46"><path d="M8 4c6-4 10 0 14 0s8-4 14 0c5 4 3 14 0 20-2 5-2 20-6 20s-4-14-8-14-4 14-8 14-4-15-6-20C5 18 3 8 8 4zM6 16h32M16 13h6v6h-6zM24 13h6v6h-6z" fill="none" stroke="#fff" stroke-width="2"/></svg>BRACES</div>
  <div class="service" style="left:841px;top:1790px"><svg width="40" height="46" viewBox="0 0 40 46"><path d="M6 6h28v10H6zM8 16c0 8 1 26 5 26s4-12 7-12 3 12 7 12 5-18 5-26" fill="none" stroke="#fff" stroke-width="2"/></svg>CROWNS</div>

  <div class="service" style="left:127px;top:1900px"><svg width="54" height="40" viewBox="0 0 54 40"><path d="M4 6c4-3 6 0 8 0s4-3 8 0 2 10 0 12H4C2 14 1 9 4 6zM34 6c4-3 6 0 8 0s4-3 8 0 2 10 0 12H34c-2-4-3-9 0-12zM20 10h14M8 22v12l3-3 3 3V22M38 22v12l3-3 3 3V22M20 22h14v10l-7 4-7-4z" fill="none" stroke="#fff" stroke-width="2"/></svg>BRIDGE</div>
  <div class="service" style="left:365px;top:1900px"><svg width="44" height="46" viewBox="0 0 44 46"><path d="M6 12c4-3 8 0 10 0s6-3 10 0c4 3 2 12 0 16s-1 14-4 14-3-10-6-10-3 10-6 10-3-10-4-14C4 24 2 15 6 12zM32 4v24M28 6l4-4 4 4M4 38h36" fill="none" stroke="#fff" stroke-width="2"/></svg>EXTRACTIONS</div>
  <div class="service" style="left:604px;top:1900px"><svg width="44" height="46" viewBox="0 0 44 46"><path d="M8 4c6-4 10 0 14 0s8-4 14 0c5 4 3 14 0 20-2 5-2 20-6 20s-4-14-8-14-4 14-8 14-4-15-6-20C5 18 3 8 8 4zM16 28c1-4 3-4 4 0M24 28c1-4 3-4 4 0" fill="none" stroke="#fff" stroke-width="2"/></svg>GUM DISEASE</div>
  <div class="service" style="left:841px;top:1900px"><svg width="52" height="48" viewBox="0 0 52 48"><path d="M14 6c6-4 10 0 12 0s6-4 12 0c5 4 3 14 0 20-2 5-2 18-6 18s-3-12-6-12-2 12-6 12-4-13-6-18c-3-6-5-16 0-20zM26 4v34M2 44h48" fill="none" stroke="#fff" stroke-width="2"/></svg>ROOT CANAL</div>

  <div class="service" style="left:129px;top:2012px"><svg width="48" height="42" viewBox="0 0 48 42"><path d="M4 8c10-6 30-6 40 0v8H4zM4 26h40v8c-10 6-30 6-40 0zM12 8v8M20 6v10M28 6v10M36 8v8M12 26v8M20 26v10M28 26v10M36 26v8" fill="none" stroke="#fff" stroke-width="2"/></svg>DENTURES</div>
  <div class="service" style="left:367px;top:2012px"><svg width="50" height="44" viewBox="0 0 50 44"><path d="M4 12h42v28H4zM16 12V6h18v6M18 20c2-2 4-1 7-1s5-1 7 1c2 3 0 8-1 10s-1 6-3 6-2-4-3-4-1 4-3 4-2-4-3-6-2-7-1-10z" fill="none" stroke="#fff" stroke-width="2"/></svg>EMERGENCY<br>DENTISTRY</div>
  <div class="service" style="left:605px;top:2012px"><svg width="50" height="46" viewBox="0 0 50 46"><path d="M4 24c4-3 7 0 9 0s5-3 9 0c3 3 2 10 0 14s-1 6-4 6-2-4-5-4-2 4-5 4-3-3-4-6c-2-4-3-11 0-14zM26 26c4-3 7 0 9 0s5-3 9 0c3 3 2 10 0 14s-1 6-4 6-2-4-5-4-2 4-5 4-3-3-4-6M30 20L44 4M40 4l4 4" fill="none" stroke="#fff" stroke-width="2"/></svg>VENEERS</div>
  <div class="service" style="left:843px;top:2012px;gap:10px;padding-left:24px"><svg width="66" height="30" viewBox="0 0 66 30"><path d="M3 8c20-6 40-6 60 0v10c-20 8-40 8-60 0zM12 7v15M21 5v18M30 4v20M39 4v20M48 5v18M56 7v15" fill="none" stroke="#fff" stroke-width="2"/></svg>CLEARLINE<br>ALIGNERS</div>
</div>

<section class="experience">
  <h2>Experience the Halvern<br><span>Dental Difference</span></h2>
  <div class="exp-rule"></div>
  <div class="exp-text">
    <p>Your smile is our #1 priority. At Halvern Dental, we provide affordable and expert dental solutions. Whether you are looking for a family dentist or have any emergency such as needing a root canal in Marlow Bay, we are here for you! We want to keep your teeth healthy inside and out. We don't just clean teeth and send you on your way, we want to know you.</p>
    <p>We accept most HMO and PPO insurances. We offer various financing options through CarePay, LendWell and In-House Plans.</p>
    <p>To constantly strive to achieve the highest level of skills and modern techniques and equipment so we can provide our patients with the best that Dentistry has to offer at our dental office in Marlow Bay, Harbor County, CA.</p>
    <p>We provide patients with the best experience you can find in all of Southern California. We provide a comfortable and friendly atmosphere to shatter any fears you may have. We supply you with all the information on your dental health options so you can feel comfortable in the choices you make, whether it's a routine check-up or dental implants in Marlow Bay.</p>
    <p>We are available for Emergency and Walk-ins.</p>
  </div>
  <div class="review-card">
    <div class="rc-title">AVERAGE RATING</div>
    <div class="rc-rating"><span class="stars">★★★★★</span> 4.9</div>
    <div class="rc-count"><i></i>126 Reviews</div>
    <div class="rc-sources"><span>Reviewly</span><span>Listora</span><span>Friendbook</span></div>
    <svg class="rc-arrow" style="left:34px" width="10" height="16" viewBox="0 0 10 16"><path d="M8 2L2 8l6 6" fill="none" stroke="#0094d4" stroke-width="2"/></svg>
    <svg class="rc-arrow" style="left:276px" width="10" height="16" viewBox="0 0 10 16"><path d="M2 2l6 6-6 6" fill="none" stroke="#0094d4" stroke-width="2"/></svg>
    <div class="rc-review">
      <div class="rc-avatar" role="img" aria-label="Reviewer profile photo"></div>
      <div class="rc-stars stars">★★★★★</div>
      <div class="rc-name">Dana Whitfield</div>
      <div class="rc-quote">Dr. Orsen and her staff are awesome! Everyone is so nice and pleasant. I always have a great experience! I don't ever feel rushed and time is taken to answer questions and make sure we are on the same page! This office i... <b>more</b></div>
      <div class="rc-date">26 February, 2021</div>
    </div>
    <div class="rc-source"><span>Source:</span><strong>Reviewly</strong></div>
  </div>
</section>

<section class="excellence" role="img" aria-label="Dentist and smiling patient in a treatment room, blue overlay">
  <h2>Committed to Excellence <span>in Oral Health Care</span></h2>
  <p class="sub">Free Exam and X-Rays for New Patients</p>
  <div class="btn btn-teal">BOOK AN APPOINTMENT</div>
</section>

<footer>
  <div class="footer-head" style="left:145px">HALVERN DENTAL</div>
  <div class="footer-rule" style="left:145px;width:174px"></div>
  <div class="footer-head" style="left:476px">OFFICE HOURS</div>
  <div class="footer-rule" style="left:476px;width:167px"></div>
  <div class="footer-head" style="left:764px">OUR LOCATION</div>
  <div class="footer-rule" style="left:764px;width:170px"></div>

  <svg class="abs" style="left:146px;top:3381px" width="14" height="20" viewBox="0 0 14 20"><path d="M7 0a7 7 0 0 1 7 7c0 5-7 13-7 13S0 12 0 7a7 7 0 0 1 7-7z" fill="#0d5f86"/><circle cx="7" cy="7" r="2.6" fill="#fff"/></svg>
  <div class="f-line" style="left:174px;top:3380px">48 Linden Grove Ave., Suite A<br>Marlow Bay, CA 90210</div>
  <svg class="abs" style="left:146px;top:3444px" width="16" height="16" viewBox="0 0 16 16"><path d="M3 1h3l1.5 3.5-2 1.5a8 8 0 0 0 4.5 4.5l1.5-2L15 10v3c-7 1-13-5-12-12z" fill="none" stroke="#0d5f86" stroke-width="1.5"/></svg>
  <div class="f-line" style="left:174px;top:3441px">Call Us: (555) 014-7720</div>
  <svg class="abs" style="left:146px;top:3475px" width="17" height="13" viewBox="0 0 17 13"><rect width="17" height="13" fill="#0d5f86"/><path d="M1 1l7.5 6L16 1" fill="none" stroke="#fff" stroke-width="1.3"/></svg>
  <div class="f-line" style="left:174px;top:3470px">hello@myhalverndental.com</div>
  <div class="btn btn-red">BOOK AN APPOINTMENT</div>

  <div class="hours">
    <span style="left:476px;top:3382px">Monday:</span><span style="left:591px;top:3382px">10AM–7PM</span>
    <span style="left:476px;top:3411px">Tuesday:</span><span style="left:591px;top:3411px">10AM–7PM</span>
    <span style="left:476px;top:3441px">Wednesday:</span><span style="left:591px;top:3441px">9AM–6PM</span>
    <span style="left:476px;top:3470px">Thursday:</span><span style="left:591px;top:3470px">9AM–6PM</span>
    <span style="left:476px;top:3499px">Friday:</span><span style="left:591px;top:3499px">9AM–5PM</span>
    <span style="left:476px;top:3528px">Saturday:</span><span style="left:591px;top:3528px">9AM–1PM</span>
  </div>

  <div class="map" role="img" aria-label="Street map showing the office location"></div>

  <div class="bottom-bar"></div>
  <nav class="bottom-nav">
    <a style="left:148px">About Us</a>
    <a style="left:234px">Services</a>
    <a style="left:317px">Financing</a>
    <a style="left:407px">Testimonials</a>
    <a style="left:511px">New Patient Visit</a>
    <a style="left:641px">Specials</a>
    <a style="left:724px">Contact Us</a>
    <a style="left:822px">Blog</a>
  </nav>
  <span class="social" style="left:939px"></span>
  <span class="social" style="left:969px"></span>
  <span class="social" style="left:999px"></span>
  <span class="social" style="left:1029px"></span>
  <span class="social" style="left:1058px"></span>
  <div class="copy">2021 MyHalvern Dental &nbsp;| &nbsp; All Rights Reserved</div>
</footer>

</body>
</html>
```